Zeitloses Etiketten-Design für Zirbenlikör gesucht
Zielgruppe
Wir sind ein Betrieb der kunsthandwerkliche Gegenstände aus Holz herstellt, vor allem aus Zirbe. Da wir seit 3 Jahren auch Zirbenlikör herstellen, suchen wir für diese ein neues Etikett.
Aufgabenstellung
Zirbelikör wird aus den Zapfen der Zirbe hergestellt. Auf der Zirbe wachsen die Zapfen das erste mal nach ca. 20 Jahren. Sie wächst in ca. 1500 - 2500m Seehöhe und ist sehr wiederstandsfähig. Die Typische Farbe des Likörs ist Dunkelrot.
Ein paar dieser Dinge sollte man dem Etikett wieder finden. Vielleicht auch Berge im Hintergrund...
Klassisch, Zeitlos, Edel, vl. auch verspielt ( vor allem das Wort Zirbe), Wiedererkennungswert und meinen Namen: KESTLER
Die Adresse kann gerne auch seitlich stehen.
Das alte Etikett habe ich selbst gemacht, es ist 6,5x10,5 cm. Fürs erste nicht so schlecht, zum expandieren eine Katastrophe.

```html
<!DOCTYPE html>
<html lang="de">
<head>
<meta charset="utf-8">
<title>Hausgemachter Zirbenlikör – Etikett</title>
<link href="https://fonts.googleapis.com/css2?family=Fira+Sans:wght@300;400&family=Italianno&display=swap" rel="stylesheet">
<style>
  :root {
    --paper: #ffffff;
    --frame-red: #d9403a;
    --liqueur-red: #9c1a12;
    --ink: #1a1a1a;
    --cone-light: #a3302b;
    --cone-mid: #6e2420;
    --cone-dark: #3a2320;
  }
  * { margin: 0; padding: 0; box-sizing: border-box; }
  html, body {
    width: 743px;
    height: 1200px;
    overflow: hidden;
    background: var(--paper);
  }
  .label {
    position: relative;
    width: 743px;
    height: 1200px;
    background: var(--paper);
  }
  .label-frame {
    position: absolute;
    left: 23px;
    top: 23px;
    width: 699px;
    height: 1149px;
    border: 2px solid var(--frame-red);
  }
  .cone-illustration {
    position: absolute;
    left: 256px;
    top: 78px;
    width: 230px;
    height: 368px;
    background: linear-gradient(110deg, var(--cone-light) 0%, var(--cone-mid) 55%, var(--cone-dark) 100%);
  }
  .product-name {
    position: absolute;
    left: 0;
    width: 743px;
    text-align: center;
    white-space: nowrap;
  }
  .product-name__prefix {
    top: 540px;
    font-family: "Fira Sans", sans-serif;
    font-weight: 300;
    font-size: 46px;
    line-height: 1.2;
    color: var(--ink);
  }
  .product-name__main {
    top: 604px;
    font-family: "Italianno", cursive;
    font-size: 196px;
    line-height: 1;
    color: var(--liqueur-red);
  }
  .product-name__main span {
    display: inline-block;
    transform: scaleX(1.25);
  }
  .product-name__type {
    top: 762px;
    font-family: "Fira Sans", sans-serif;
    font-weight: 300;
    font-size: 112px;
    line-height: 1.2;
    color: var(--liqueur-red);
  }
  .producer-address {
    position: absolute;
    left: 0;
    top: 1121px;
    width: 743px;
    display: flex;
    justify-content: center;
    gap: 26px;
    font-family: "Fira Sans", sans-serif;
    font-weight: 400;
    font-size: 29px;
    line-height: 1.2;
    color: var(--ink);
  }
</style>
</head>
<body>
  <main class="label">
    <div class="label-frame"></div>

    <div class="cone-illustration" role="img" aria-label="Illustration eines dunkelroten Zirbenzapfens"></div>

    <div class="product-name product-name__prefix">Hausgemachter</div>
    <div class="product-name product-name__main"><span>Zirben</span></div>
    <div class="product-name product-name__type">LIKÖR</div>

    <footer class="producer-address">
      <span>T. Kestler</span>
      <span>Lärchenweg Gasse 14</span>
      <span>3580 Brunnfeld</span>
    </footer>
  </main>
</body>
</html>
```